Property Developer - Simple yet Sophisticated and Sharp Business Card

We are a medium sized property developer involved mainly in townhouse developments and land subdivisions.

The company is looking for a simple, sharp and sophisticated business card that will be given to contractors, land owners, financiers etc and thus will need to look professional.

Property development related graphics and art can be used, however the card is not to be too "busy" or crowded. Our company name is KL Estates which could possibly be incorporated into the graphics or artwork.

Single sided and/or double sided designs will be acceptable.

A Simple, Sophisticated, Sharp design please!

Good Luck !

```html
<!DOCTYPE html>
<html lang="en">
<head>
<meta charset="utf-8">
<title>KL Estates – Business Card</title>
<link href="https://fonts.googleapis.com/css2?family=Arimo:wght@400&display=swap" rel="stylesheet">
<style>
  :root {
    --backdrop: #dcdcdc;
    --card-top: #ffffff;
    --card-bottom: #ececec;
    --brand-red: #b71c2b;
    --text-grey: #6e6e6e;
    --text-dark: #4a4a4a;
  }
  * { margin: 0; padding: 0; box-sizing: border-box; }
  html, body {
    width: 1200px;
    height: 900px;
    overflow: hidden;
    background: var(--backdrop);
    font-family: "Arimo", Arial, sans-serif;
  }
  .business-card {
    position: absolute;
    left: 100px;
    top: 166px;
    width: 1000px;
    height: 568px;
    background: linear-gradient(180deg, var(--card-top) 0%, var(--card-bottom) 100%);
  }
  .brand {
    position: absolute;
    left: 34px;
    top: 42px;
    display: flex;
    align-items: center;
    gap: 22px;
  }
  .brand-square {
    width: 74px;
    height: 74px;
    background: var(--brand-red);
  }
  .brand-name {
    font-size: 60px;
    font-weight: 400;
    color: var(--text-grey);
    letter-spacing: 1px;
  }
  .person {
    position: absolute;
    left: 0;
    right: 0;
    top: 236px;
    text-align: center;
  }
  .person-name {
    font-size: 56px;
    color: var(--brand-red);
    line-height: 1;
  }
  .person-role {
    margin-top: 10px;
    font-size: 34px;
    color: var(--text-grey);
    line-height: 1;
  }
  .contact {
    position: absolute;
    left: 38px;
    top: 448px;
    font-size: 27px;
    line-height: 34px;
    border-collapse: collapse;
  }
  .contact td { padding: 0; white-space: nowrap; }
  .contact-label { color: var(--brand-red); width: 89px; }
  .contact-colon { color: var(--text-dark); width: 26px; }
  .contact-value { color: var(--text-dark); }
  .divider {
    position: absolute;
    left: 600px;
    top: 434px;
    width: 5px;
    height: 128px;
    background: var(--brand-red);
  }
  .address {
    position: absolute;
    left: 661px;
    top: 448px;
    font-size: 27px;
    line-height: 34px;
    color: var(--text-grey);
  }
  .address-country { color: var(--brand-red); }
</style>
</head>
<body>
  <main class="business-card">
    <div class="brand">
      <div class="brand-square"></div>
      <div class="brand-name">KL Estates</div>
    </div>

    <div class="person">
      <div class="person-name">Daniel Orsay</div>
      <div class="person-role">Designer</div>
    </div>

    <table class="contact">
      <tr><td class="contact-label">email</td><td class="contact-colon">:</td><td class="contact-value">daniel@klestates.com</td></tr>
      <tr><td class="contact-label">tel</td><td class="contact-colon">:</td><td class="contact-value">+61-2-5550-1847</td></tr>
      <tr><td class="contact-label">web</td><td class="contact-colon">:</td><td class="contact-value">http://www.klestates.com</td></tr>
    </table>

    <div class="divider"></div>

    <address class="address" style="font-style: normal;">
      <div>Suite 12, 48 Harbour Ln,</div>
      <div>Sydney, NSW 2000</div>
      <div class="address-country">Australia</div>
    </address>
  </main>
</body>
</html>
```